tilebaron.org needs a cool website!

I need a website designed for a commercial flooring maintenance company based in Texas. We will be providing services like carpet shampooing, burnishing, resurfacing and power washing. It needs to be cool and trendy.

I’ll need 10-20 pages. I need help deciding on the style and color palette. We will need great stock pictures of different flooring types and you will need to photo shop our logo on imaginary cars or storefronts.

Please have similar experience and an open mind. I’m looking for a partnership and someone to turn to for future projects and upkeep.

The domain is currently hosted on Wix. You will need the ability to develop and code it there.
Updates

Target Market(s)

Commercial businesses and properties

Industry/Entity Type

Floor care

Coding

Coded - Design and coding required

Number of Pages Required

5+ page

Requirements
Must have
• Great pictures of different types of floors.

```html
<!DOCTYPE html>
<html lang="en">
<head>
<meta charset="utf-8">
<title>tilebaron.org — Love Your Floor A Little More</title>
<link rel="stylesheet" href="https://fonts.googleapis.com/css2?family=Lexend:wght@500;600;700&family=Poppins:wght@400;500;600;700&display=swap">
<style>
:root{
  --green:#8fad3b;
  --green-dark:#7a9630;
  --tint:#f6fde6;
  --band:#e4f6b4;
  --ink:#1f1f1f;
  --muted:#8a8a8a;
  --dark:#232323;
  --white:#ffffff;
  --line:#e8e8e8;
}
*{box-sizing:border-box;margin:0;padding:0}
html,body{width:1200px;height:4414px;overflow:hidden}
body{font-family:"Poppins",sans-serif;color:var(--ink);background:var(--white);position:relative}
.section{position:absolute;left:0;width:1200px}
.abs{position:absolute}
.h-title{font-family:"Lexend",sans-serif;font-weight:600;text-transform:uppercase;line-height:1.2;color:var(--ink)}
.h-title em{font-style:normal;color:var(--green)}
.copy{font-size:11px;line-height:23px;color:var(--muted)}
.btn{position:absolute;display:flex;align-items:center;justify-content:center;height:36px;width:134px;background:var(--green);color:var(--white);font-size:10px;font-weight:600;letter-spacing:.3px;text-transform:uppercase}
.photo{position:absolute}

/* hero */
.hero{top:0;height:596px;background:var(--tint)}
.brand{display:flex;align-items:center;gap:8px;font-family:"Poppins",sans-serif;font-size:21px;font-weight:500;color:var(--ink)}
.brand .dot{width:12px;height:12px;border-radius:50%;background:var(--ink)}
.nav{left:451px;top:36px;display:flex;gap:32px;font-size:11px;font-weight:500}
.hero-photo{left:789px;top:0;width:411px;height:596px;border-radius:0 0 0 260px / 0 0 0 300px;background:linear-gradient(160deg,#d9d4cc,#b9a27d 55%,#8f7a5a)}
.play{width:76px;height:76px;border-radius:50%;background:var(--green);box-shadow:0 0 0 9px rgba(143,173,59,.35);display:flex;align-items:center;justify-content:center}
.play-sm{width:36px;height:36px;border-radius:50%;background:var(--green);box-shadow:0 0 0 5px rgba(143,173,59,.3);display:flex;align-items:center;justify-content:center}

/* partners */
.partner{display:flex;align-items:center;gap:8px;font-family:"Poppins",sans-serif;font-weight:600;font-size:19px;color:#b6b6b6}
.partner .mark{width:22px;height:22px;border-radius:50%;border:2px solid #b6b6b6}
.partner.first{color:var(--ink)}
.partner.first .mark{border-color:var(--green);background:var(--green)}

/* services */
.service{position:absolute;top:901px;width:194px;height:198px;padding:30px 18px}
.service.featured{background:var(--white);box-shadow:0 10px 40px rgba(0,0,0,.08)}
.service .ico{width:52px;height:52px;border-radius:50%;background:#eef7d5;display:flex;align-items:center;justify-content:center;margin-bottom:20px}
.service h3{font-size:11px;font-weight:600;text-transform:uppercase;margin-bottom:8px}
.service p{font-size:11px;line-height:19px;color:var(--muted)}

/* feedback */
.review{position:absolute;top:2762px;width:268px;height:244px;background:var(--white);border-top:5px solid var(--ink);padding:26px 26px}
.review .quote{font-family:"Lexend",sans-serif;font-size:34px;line-height:24px;color:var(--green);font-weight:700;height:28px}
.review p{font-size:9.5px;line-height:23px;color:var(--muted);margin-top:4px}
.person{display:flex;align-items:center;gap:10px;margin-top:12px;font-size:10px;font-weight:600;text-transform:uppercase}
.avatar{width:40px;height:40px;border-radius:50%;background:#9aa3b0}
.arrow-sq{position:absolute;width:32px;height:32px;background:var(--white);display:flex;align-items:center;justify-content:center}

/* blog */
.post{position:absolute;top:3581px;width:265px;height:373px;background:var(--white);box-shadow:0 8px 40px rgba(0,0,0,.07);padding:18px}
.post .frame{border:1.5px dashed var(--green);padding:5px;height:170px}
.post .frame div{width:100%;height:100%}
.post h4{font-size:11px;font-weight:600;text-transform:uppercase;margin:22px 0 10px}
.post p{font-size:9px;line-height:23px;color:var(--muted)}
.post .more{display:block;margin-top:8px;font-size:10px;font-weight:600;color:var(--green);text-transform:uppercase}
.slide-btn{position:absolute;width:32px;height:32px;background:var(--green);display:flex;align-items:center;justify-content:center}

/* footer */
.footer{top:4101px;height:270px;background:var(--dark);color:var(--white)}
.footer h5{font-family:"Lexend",sans-serif;font-size:16px;font-weight:600;text-transform:uppercase}
.footer ul{list-style:none;font-size:10px;line-height:26px}
.contact-row{display:flex;align-items:center;gap:12px;font-size:10px;margin-bottom:14px}
.contact-row .c{width:20px;height:20px;border-radius:50%;background:var(--white);display:flex;align-items:center;justify-content:center}
.bottom-bar{top:4371px;height:43px;display:flex;align-items:center;justify-content:center;font-size:10px}
</style>
</head>
<body>

<!-- HERO -->
<section class="section hero">
  <div class="abs brand" style="left:187px;top:28px"><span class="dot"></span>tilebaron.org</div>
  <nav class="abs nav"><span>Home</span><span>How It Works</span><span>Services</span><span>Our Projects</span></nav>
  <div class="photo hero-photo" role="img" aria-label="Cleaner in yellow gloves mopping a light wooden office floor"></div>
  <div class="btn" style="left:878px;top:26px;width:135px">Contact Us</div>
  <h1 class="abs h-title" style="left:187px;top:202px;font-size:41px;line-height:50px">Love Your<br>Floor A <em>Little More</em></h1>
  <p class="abs copy" style="left:187px;top:314px;width:470px;line-height:19px">Lorem Ipsum is simply dummy text of the printing and typesetting industry.<br>Lorem Ipsum has been the industry's .</p>
  <div class="btn" style="left:187px;top:384px">Read More</div>
  <div class="abs play-sm" style="left:339px;top:384px"><svg width="12" height="12" viewBox="0 0 12 12"><path d="M3 1l8 5-8 5z" fill="#fff"/></svg></div>
  <span class="abs" style="left:384px;top:395px;font-size:10px;color:var(--muted)">How It Works .</span>
  <div class="abs play" style="left:751px;top:257px"><svg width="22" height="22" viewBox="0 0 22 22"><path d="M5 2l15 9-15 9z" fill="#fff"/></svg></div>
</section>

<!-- PARTNERS -->
<div class="abs partner first" style="left:187px;top:671px"><span class="mark"></span>Yourlogo</div>
<div class="abs partner" style="left:358px;top:671px"><span class="mark"></span>Yourlogo</div>
<div class="abs partner" style="left:528px;top:671px"><span class="mark"></span>Yourlogo</div>
<div class="abs partner" style="left:699px;top:671px"><span class="mark"></span>Yourlogo</div>
<div class="abs partner" style="left:869px;top:671px"><span class="mark"></span>Yourlogo</div>

<!-- SERVICES -->
<h2 class="abs h-title" style="left:0;width:1200px;text-align:center;top:764px;font-size:37px;line-height:50px">Shine Brighter<br>With Expert <em>Floor Care</em></h2>
<div class="service featured" style="left:187px">
  <div class="ico"><svg width="24" height="24" viewBox="0 0 24 24" fill="none" stroke="#8fad3b" stroke-width="1.5"><rect x="4" y="3" width="10" height="16"/><path d="M14 8h5v11h-5M4 21h16"/></svg></div>
  <h3>Carpet Shampooing</h3><p>Lorem Ipsum is simply dummy text of the printing and typesetting</p>
</div>
<div class="service" style="left:399px">
  <div class="ico"><svg width="24" height="24" viewBox="0 0 24 24" fill="none" stroke="#8fad3b" stroke-width="1.5"><rect x="4" y="4" width="16" height="16" rx="2"/><path d="M8 16l8-8M9 9h2M13 15h2"/></svg></div>
  <h3>Burnishing</h3><p>Lorem Ipsum is simply dummy text of the printing and typesetting</p>
</div>
<div class="service" style="left:609px">
  <div class="ico"><svg width="24" height="24" viewBox="0 0 24 24" fill="none" stroke="#8fad3b" stroke-width="1.5"><path d="M3 15h14l3-4h-6l-2-3H5z"/><circle cx="7" cy="18" r="2"/><circle cx="15" cy="18" r="2"/></svg></div>
  <h3>Resurfacing</h3><p>Lorem Ipsum is simply dummy text of the printing and typesetting</p>
</div>
<div class="service" style="left:819px">
  <div class="ico"><svg width="24" height="24" viewBox="0 0 24 24" fill="none" stroke="#8fad3b" stroke-width="1.5"><path d="M4 6h12a3 3 0 010 6H8a3 3 0 000 6h12"/><circle cx="18" cy="18" r="1.5"/></svg></div>
  <h3>Power Washing</h3><p>Lorem Ipsum is simply dummy text of the printing and typesetting</p>
</div>

<!-- CREATE YOUR OWN FLOORING -->
<section class="section" style="top:1175px;height:393px;background:var(--tint)">
  <h2 class="abs h-title" style="left:187px;top:68px;font-size:31px;line-height:44px">Create Your Own<br><em>Flooring</em></h2>
  <p class="abs copy" style="left:187px;top:162px;width:390px">Lorem Ipsum is simply dummy text of the printing and typesetting industry. Lorem Ipsum has been the industry's standard dummy text ever since the 1500s, when an unknown printer took a galley of type and scrambled it to make a type specimen book. It has survived not only five centuries .</p>
  <div class="btn" style="left:187px;top:281px">More About</div>
  <div class="photo" role="img" aria-label="Friends sitting on a polished wooden floor in a bright open-plan living room" style="left:643px;top:77px;width:389px;height:242px;background:linear-gradient(135deg,#e9e6e0,#c9b79b 60%,#9b7d58)"></div>
</section>

<!-- RECENT PROJECTS -->
<h2 class="abs h-title" style="left:0;width:1200px;text-align:center;top:1632px;font-size:31px">Our Recent <em>Projects</em></h2>
<div class="photo" role="img" aria-label="Wooden-panelled room with a grey sofa" style="left:93px;top:1786px;width:149px;height:203px;background:linear-gradient(160deg,#b5823f,#7c4e22)"></div>
<div class="photo" role="img" aria-label="Cleaner with a mop and bucket in a white kitchen" style="left:257px;top:1755px;width:195px;height:264px;background:linear-gradient(160deg,#eeeeee,#c9cbcd)"></div>
<div class="photo" role="img" aria-label="Sunlit living room with oak plank flooring" style="left:468px;top:1715px;width:265px;height:344px;background:linear-gradient(170deg,#f1efea,#c9b496 60%,#a88f6b)"></div>
<div class="photo" role="img" aria-label="Cleaner in an apron mopping a white floor" style="left:748px;top:1755px;width:195px;height:264px;background:linear-gradient(160deg,#f4f4f4,#cfd3d8)"></div>
<div class="photo" role="img" aria-label="Loft bedroom with concrete walls and wooden floor" style="left:959px;top:1786px;width:149px;height:203px;background:linear-gradient(160deg,#6a5c4e,#b59c7c)"></div>
<div class="btn" style="left:532px;top:2095px">View All</div>

<!-- READY FOR A REFRESH -->
<section class="section" style="top:2210px;height:473px;background:var(--tint)">
  <div class="photo" role="img" aria-label="Cleaner vacuuming a wooden floor" style="left:187px;top:72px;width:161px;height:160px;background:linear-gradient(160deg,#d8d2c7,#9c8466)"></div>
  <div class="photo" role="img" aria-label="Gloved hand wiping a floor with a yellow cloth" style="left:297px;top:93px;width:290px;height:292px;background:linear-gradient(150deg,#d7d6d3,#e7d46a 60%,#f2f0e8);border:3px solid var(--white)"></div>
  <div class="photo" role="img" aria-label="Cleaner mopping a white room" style="left:447px;top:237px;width:164px;height:162px;background:linear-gradient(160deg,#e9e9e7,#b0a895);border:3px solid var(--white)"></div>
  <h2 class="abs h-title" style="left:680px;top:77px;font-size:37px;line-height:45px">Ready<br>For <em>A Refresh?</em></h2>
  <p class="abs copy" style="left:680px;top:180px;width:330px">Lorem Ipsum is simply dummy text of the printing and typesetting industry. Lorem Ipsum has been the industry's standard dummy text ever since the 1500s, when an unknown printer took a galley of type and scrambled it to make a type specimen book. It has survived not only five centuries .</p>
  <div class="btn" style="left:680px;top:344px">Contact Us</div>
</section>

<!-- FEEDBACK -->
<h2 class="abs h-title" style="left:187px;top:2744px;font-size:37px;line-height:44px">Our Clients<br>&amp; Thier <em>Feedback</em></h2>
<p class="abs copy" style="left:187px;top:2844px;width:380px">Lorem Ipsum is simply dummy text of the printing and typesetting industry. Lorem Ipsum has been the industry's standard dummy text ever since the 1500s, when an unknown printer took a galley of type and scrambled it to make a type specimen book. It has survived not only five centuries .</p>
<div class="btn" style="left:187px;top:2990px">View All</div>
<div class="abs" style="left:608px;top:2762px;width:592px;height:316px;background:var(--green)"></div>
<div class="abs" style="left:752px;top:3078px;width:76px;height:77px;background:#d9d9d9"></div>
<div class="review" style="left:656px">
  <div class="quote">“</div>
  <p>Lorem Ipsum is simply dummy text of the printing and typesetting industry. Lorem Ipsum has been the industry's standard dummy text ever since the 1500s, when an unknown printer took a galley of type .</p>
  <div class="person"><span class="avatar" role="img" aria-label="Client portrait"></span>John Doe</div>
</div>
<div class="review" style="left:935px">
  <div class="quote">“</div>
  <p>Lorem Ipsum is simply dummy text of the printing and typesetting industry. Lorem Ipsum has been the industry's standard dummy text ever since the 1500s, when an unknown printer took a galley of type .</p>
  <div class="person"><span class="avatar" role="img" aria-label="Client portrait" style="background:#b49aa6"></span>Maria</div>
</div>
<div class="arrow-sq" style="left:656px;top:3023px"><svg width="12" height="12" viewBox="0 0 12 12"><path d="M8 2L4 6l4 4" stroke="#8fad3b" stroke-width="2" fill="none"/></svg></div>
<div class="arrow-sq" style="left:704px;top:3023px"><svg width="12" height="12" viewBox="0 0 12 12"><path d="M4 2l4 4-4 4" stroke="#8fad3b" stroke-width="2" fill="none"/></svg></div>

<!-- CTA BAND -->
<section class="section" style="top:3155px;height:268px;background:var(--band)">
  <h2 class="abs h-title" style="left:187px;top:90px;font-size:37px;line-height:44px">Tile<br>Baron <em>. Org</em></h2>
  <div class="abs" style="left:475px;top:100px;width:1px;height:70px;background:var(--ink)"></div>
  <p class="abs copy" style="left:519px;top:64px;width:380px">Lorem Ipsum is simply dummy text of the printing and typesetting industry. Lorem Ipsum has been the industry's standard dummy text ever since the 1500s,</p>
  <div class="btn" style="left:519px;top:153px;background:var(--dark)">Contact Us</div>
  <div class="photo" role="img" aria-label="Brand mascot artwork" style="left:968px;top:18px;width:172px;height:230px;background:linear-gradient(180deg,#cfe69a,#b8d77a)"></div>
</section>

<!-- BLOG -->
<h2 class="abs h-title" style="left:0;width:1200px;text-align:center;top:3488px;font-size:37px">From Our <em>Blog</em></h2>
<div class="slide-btn" style="left:130px;top:3744px"><svg width="12" height="12" viewBox="0 0 12 12"><path d="M8 2L4 6l4 4" stroke="#fff" stroke-width="2" fill="none"/></svg></div>
<div class="slide-btn" style="left:1038px;top:3750px"><svg width="12" height="12" viewBox="0 0 12 12"><path d="M4 2l4 4-4 4" stroke="#fff" stroke-width="2" fill="none"/></svg></div>
<article class="post" style="left:187px">
  <div class="frame"><div role="img" aria-label="Living room with tall windows and wood floor" style="background:linear-gradient(160deg,#dfe3e6,#7e8a96 60%,#a58a66)"></div></div>
  <h4>Lorem Ipsum Is Simply</h4>
  <p>Lorem Ipsum is simply dummy text of the printing and typesetting industry. Lorem Ipsum has been the industry's standard dummy text ever since the 1500s,</p>
  <span class="more">Read More</span>
</article>
<article class="post" style="left:467px">
  <div class="frame"><div role="img" aria-label="Cleaner mopping a kitchen floor" style="background:linear-gradient(160deg,#8c8c8c,#bfbfbf 60%,#a6a096)"></div></div>
  <h4>Lorem Ipsum Is Simply</h4>
  <p>Lorem Ipsum is simply dummy text of the printing and typesetting industry. Lorem Ipsum has been the industry's standard dummy text ever since the 1500s,</p>
  <span class="more">Read More</span>
</article>
<article class="post" style="left:748px">
  <div class="frame"><div role="img" aria-label="Red mop bucket and yellow cloths on a floor" style="background:linear-gradient(160deg,#5d6a7a,#c84a3a 50%,#e5c64a)"></div></div>
  <h4>Lorem Ipsum Is Simply</h4>
  <p>Lorem Ipsum is simply dummy text of the printing and typesetting industry. Lorem Ipsum has been the industry's standard dummy text ever since the 1500s,</p>
  <span class="more">Read More</span>
</article>
<div class="btn" style="left:532px;top:3986px">View All</div>

<!-- FOOTER -->
<footer class="section footer">
  <div class="abs brand" style="left:187px;top:76px;color:var(--white);font-size:27px"><span class="dot" style="background:var(--white)"></span>tilebaron.org</div>
  <p class="abs" style="left:187px;top:152px;width:300px;font-size:10px;line-height:23px">Lorem Ipsum is simply dummy text of the printing and typesetting industry.</p>
  <h5 class="abs" style="left:581px;top:72px">Quick Links</h5>
  <ul class="abs" style="left:581px;top:110px"><li>Home</li><li>About</li><li>Our Services</li><li>Help &amp; Support</li></ul>
  <h5 class="abs" style="left:802px;top:72px">Contact Info</h5>
  <div class="abs" style="left:802px;top:114px">
    <div class="contact-row"><span class="c"><svg width="10" height="10" viewBox="0 0 24 24"><path d="M6 2l4 4-2 3a12 12 0 007 7l3-2 4 4-3 4C10 22 2 14 2 5z" fill="#232323"/></svg></span>5550192834</div>
    <div class="contact-row"><span class="c"><svg width="10" height="10" viewBox="0 0 24 24"><rect x="2" y="5" width="20" height="14" fill="#232323"/></svg></span>hello@tilebaron.org</div>
  </div>
</footer>
<div class="section bottom-bar">Copyright@2024-Tile Baron . Org</div>

</body>
</html>
```